Business Cards and Stationery for Health business
Wellmorrow PLLC
Thanks
Pls check private messages
Please include with your business card design:
stationery
fax cover sheet
envelopes
Thank you very much!
Also extremely important not to have a white background. It is way too bright for my concept. I want to convey a soft flowing feeling. I like a pale peach-colored background integrated with your design. If you use green to teal colors notice in the logo how they fade into one another to give the vision of continuity. They are not separated. That was intentional.
For informational purposes, the address on the card is a mailing address only. It is optional to be included.
I hope this helps.
Thank you once again!
TR/PNK/DV Team
You may leave off the street address. That will create more room. Please place individual's name and licenses close. They belong to the individual and not to the company
Please no not overpower with green (very common color used in health) and please try to create a warm and flowing effect. In the logo an important aspect was the gradual "flow" of "bridge" from the green to the teal in the word "Wellmorrow" to illustrate the connectivity and continuity. Please try to avoid straight lines or angles. I believe that no path in life runs a straight course. Perhaps a non-over powering mild wave pattern design could be incorporated.
Thank you!
I have learned that even though I have trademarked the word Wellmorrow, the company name cannot include the ®. There fore the company name must be written as Wellmorrow PLLC.
I apologize for the confusion. For the designs already entered..no problem...I will just request the change is I choose one of those. But this applies to the new entries.
Thank all of you very talented people for your entries!
On the back (top half) of the business card please list the following four items in bulleted form:
Health Coaching
Patient Navigation
Patient Advocacy
Health Information Consulting
Thank you! :)

```html
<!DOCTYPE html>
<html lang="en">
<head>
<meta charset="utf-8">
<title>Wellmorrow PLLC — Business Card</title>
<link href="https://fonts.googleapis.com/css2?family=Open+Sans:wght@400;600;700&family=PT+Serif:wght@400;700&display=swap" rel="stylesheet">
<style>
  :root {
    --backdrop: #e8e3dc;
    --card-front: #fdf6ef;
    --peach: #fbe6d4;
    --teal: #3db4d8;
    --teal-deep: #1c9cc4;
    --green: #7dbb42;
    --orange: #f39a3a;
    --ink: #3d3d3d;
    --ink-soft: #5c5c5c;
    --back-top: #f3fbfe;
    --back-bottom: #cdeef8;
    --line: #7a8a90;
  }
  * { box-sizing: border-box; margin: 0; padding: 0; }
  html, body { width: 1200px; height: 401px; overflow: hidden; }
  body { background: var(--backdrop); font-family: "Open Sans", sans-serif; color: var(--ink); position: relative; }

  .card { position: absolute; top: 24px; width: 574px; height: 353px; border-radius: 14px; overflow: hidden; box-shadow: 0 2px 8px rgba(0,0,0,.18); }

  /* Front */
  .card-front { left: 19px; background: linear-gradient(135deg, var(--card-front), var(--peach)); }
  .front-panel { position: absolute; inset: 0; }
  .brand { position: absolute; left: 22px; top: 30px; display: flex; align-items: center; gap: 8px; }
  .brand-dot { width: 22px; height: 22px; border-radius: 50%; background: var(--green); }
  .brand-name { font-family: "Open Sans", sans-serif; font-weight: 700; font-size: 22px; color: var(--green); letter-spacing: .3px; }
  .brand-tagline { position: absolute; left: 54px; top: 60px; font-size: 8px; font-style: italic; color: var(--ink-soft); }
  .accent-art { position: absolute; left: 150px; top: 95px; width: 140px; height: 150px; }
  .holder { position: absolute; left: 24px; top: 208px; width: 230px; }
  .holder-name { font-size: 15px; font-weight: 700; color: var(--ink); }
  .holder-name small { font-size: 10px; font-weight: 600; }
  .holder-title { font-size: 9.5px; line-height: 1.35; color: var(--ink-soft); margin-top: 3px; }
  .holder-licenses { position: absolute; left: 24px; top: 302px; font-size: 9.5px; line-height: 1.4; color: var(--ink-soft); }

  .address { position: absolute; left: 360px; top: 98px; font-size: 10px; line-height: 1.45; color: var(--ink); }
  .contacts { position: absolute; right: 24px; top: 180px; list-style: none; font-size: 10px; line-height: 1.85; color: var(--ink); text-align: right; }
  .contacts li { display: flex; align-items: center; justify-content: flex-end; gap: 6px; }
  .contacts svg { width: 10px; height: 10px; }

  /* Back */
  .card-back { left: 606px; background: linear-gradient(180deg, var(--back-top), var(--back-bottom)); }
  .services { position: absolute; left: 30px; top: 32px; display: grid; grid-template-columns: 148px auto; row-gap: 6px; font-size: 11.5px; color: var(--ink); }
  .back-mark { position: absolute; right: 36px; top: 64px; width: 56px; height: 56px; border-radius: 50%; background: radial-gradient(circle at 40% 40%, #d7f0dd, #b9e4ef); }
  .appointment { position: absolute; left: 30px; top: 110px; width: 520px; }
  .appointment h2 { font-family: "PT Serif", serif; font-weight: 400; font-size: 19px; color: var(--ink); letter-spacing: .5px; }
  .field-row { display: flex; align-items: flex-end; font-size: 12px; margin-top: 12px; gap: 6px; }
  .field-line { border-bottom: 1px solid var(--line); height: 14px; }
  .days { display: flex; gap: 8px; margin-top: 18px; }
  .day { display: flex; align-items: center; gap: 5px; font-size: 11px; font-weight: 700; }
  .day-box { width: 36px; height: 18px; border: 1px solid var(--line); border-radius: 3px; background: #fff; }
  .notice { font-size: 10.5px; font-style: italic; margin-top: 14px; color: var(--ink-soft); }
</style>
</head>
<body>

<section class="card card-front" aria-label="Business card front">
  <svg class="front-panel" viewBox="0 0 574 353" preserveAspectRatio="none" aria-hidden="true">
    <defs>
      <linearGradient id="panelFill" x1="0" y1="0" x2="1" y2="1">
        <stop offset="0" stop-color="#5cc7e6"/>
        <stop offset="1" stop-color="#2aa6cf"/>
      </linearGradient>
    </defs>
    <path d="M300 0 H574 V353 H330 C270 300 250 220 290 150 C320 95 290 40 300 0 Z" fill="url(#panelFill)"/>
    <path d="M300 0 C290 40 320 95 290 150 C250 220 270 300 330 353" fill="none" stroke="#ffffff" stroke-width="4" opacity=".7"/>
  </svg>

  <div class="brand">
    <span class="brand-dot"></span>
    <span class="brand-name">Wellmorrow PLLC</span>
  </div>
  <p class="brand-tagline">caring for your whole self</p>

  <svg class="accent-art" viewBox="0 0 140 150" role="img" aria-label="Soft orange and green flowing accent area">
    <defs>
      <radialGradient id="accentFill" cx=".45" cy=".45" r=".6">
        <stop offset="0" stop-color="#f7b46a" stop-opacity=".55"/>
        <stop offset="1" stop-color="#a9d37a" stop-opacity="0"/>
      </radialGradient>
    </defs>
    <ellipse cx="70" cy="75" rx="68" ry="72" fill="url(#accentFill)"/>
  </svg>

  <div class="holder">
    <p class="holder-name">Dana Whitlow, <small>ANP-C, ACNP-BC</small></p>
    <p class="holder-title">President, Adult Nurse Practitioner and<br>Acute Care Nurse Practitioner</p>
  </div>
  <p class="holder-licenses">ARNP 0000000 (FL)<br>RN 000000 (MO)</p>

  <address class="address" style="font-style:normal">2210 Harbor Lane<br>Ste.40, Coral Bay, FL 33000</address>

  <ul class="contacts">
    <li>888-555-0142 (TF)
      <svg viewBox="0 0 10 10" aria-hidden="true"><path d="M2 1 L4 1 L4.6 3 L3.4 3.8 C4 5.2 4.8 6 6.2 6.6 L7 5.4 L9 6 L9 8 C5 8.5 1.5 5 2 1 Z" fill="#ffffff"/></svg>
    </li>
    <li>855-555-0187
      <svg viewBox="0 0 10 10" aria-hidden="true"><rect x="1.5" y="3" width="7" height="5" rx="1" fill="#ffffff"/><rect x="3" y="1" width="4" height="2.5" fill="#ffffff"/></svg>
    </li>
    <li>dana@wellmorrow.com
      <svg viewBox="0 0 10 10" aria-hidden="true"><rect x="1" y="2.5" width="8" height="5.5" rx=".8" fill="#ffffff"/><path d="M1.3 2.8 L5 5.6 L8.7 2.8" stroke="#2aa6cf" stroke-width=".8" fill="none"/></svg>
    </li>
    <li>www.wellmorrow.com
      <svg viewBox="0 0 10 10" aria-hidden="true"><circle cx="5" cy="5" r="3.8" fill="none" stroke="#ffffff" stroke-width="1"/><path d="M1.2 5 H8.8 M5 1.2 C3 3.5 3 6.5 5 8.8 C7 6.5 7 3.5 5 1.2" stroke="#ffffff" stroke-width=".7" fill="none"/></svg>
    </li>
  </ul>
</section>

<section class="card card-back" aria-label="Business card back">
  <ul class="services" style="list-style:none">
    <li>Health Coaching</li>
    <li>Patient Navigation</li>
    <li>Patient Advocacy</li>
    <li>Health Information Consulting</li>
  </ul>

  <div class="back-mark" aria-hidden="true"></div>

  <div class="appointment">
    <h2>YOUR APPOINTMENT</h2>
    <div class="field-row">
      <span>Name :</span><span class="field-line" style="width:250px"></span>
    </div>
    <div class="field-row">
      <span>Date :</span><span class="field-line" style="width:110px"></span>
      <span>&nbsp;&nbsp;Time :</span><span class="field-line" style="width:110px"></span>
      <span>am / pm</span>
    </div>
    <div class="days">
      <span class="day">MON <span class="day-box"></span></span>
      <span class="day">TUE <span class="day-box"></span></span>
      <span class="day">WED <span class="day-box"></span></span>
      <span class="day">THU <span class="day-box"></span></span>
      <span class="day">FRI <span class="day-box"></span></span>
      <span class="day">SAT <span class="day-box"></span></span>
    </div>
    <p class="notice">If unable to keep your appointment, Kindly give 24 hours notice</p>
  </div>
</section>

</body>
</html>
```